Copperleaf Grill
there is none
Copperleaf Grill -
Simple
Danielle Whitcomb
Proprietor
318 Ferrand Street New Orleans, LA 70119
dwhitcomb@copperleaf-eats.com
www.copperleaf-eats.com
Use the same font of Grill and New Orleans for information on card
Just put the logo and website on the back of the card

```html
<!DOCTYPE html>
<html lang="en">
<head>
<meta charset="utf-8">
<title>Copperleaf Grill – Business Card</title>
<link rel="stylesheet" href="https://fonts.googleapis.com/css2?family=Arimo:wght@400;700&display=swap">
<style>
  :root {
    --page: #ffffff;
    --maroon: #8c2a35;
    --maroon-deep: #3f0810;
    --maroon-glow: #8a2232;
    --ink: #4a4a4a;
    --ink-soft: #7a7a7a;
    --card-light: #ffffff;
    --card-grey: #bdbdbd;
    --back-text: #f3e6e8;
  }
  html, body {
    margin: 0;
    padding: 0;
    width: 1200px;
    height: 475px;
    overflow: hidden;
    background: var(--page);
    font-family: "Arimo", Arial, sans-serif;
  }
  .canvas {
    position: relative;
    width: 1200px;
    height: 475px;
  }
  .card {
    position: absolute;
    top: 72px;
    width: 504px;
    height: 340px;
    border-radius: 24px;
    overflow: hidden;
    box-shadow: 0 2px 6px rgba(0,0,0,0.25);
  }
  .card-front {
    left: 80px;
    background: linear-gradient(90deg, var(--card-light) 0%, #f1f1f1 45%, var(--card-grey) 100%);
  }
  .card-back {
    left: 629px;
    background: radial-gradient(circle at 25% 45%, var(--maroon-glow) 0%, #5e1220 38%, var(--maroon-deep) 80%);
  }
  .brand {
    position: absolute;
    left: 22px;
    top: 42px;
    display: flex;
    align-items: center;
    gap: 8px;
  }
  .brand-mark {
    width: 14px;
    height: 14px;
    border-radius: 50%;
    background: var(--maroon);
  }
  .brand-name {
    font-weight: 700;
    font-size: 22px;
    color: var(--maroon);
    letter-spacing: -0.3px;
  }
  .brand-city {
    position: absolute;
    left: 44px;
    top: 74px;
    font-size: 9px;
    letter-spacing: 3px;
    color: var(--ink-soft);
    text-transform: uppercase;
  }
  .artwork {
    position: absolute;
    border-radius: 50% 40% 45% 50%;
  }
  .artwork-front {
    left: 330px;
    top: 48px;
    width: 174px;
    height: 156px;
    background: var(--maroon);
    opacity: 0.9;
  }
  .artwork-back {
    left: 18px;
    top: 40px;
    width: 150px;
    height: 190px;
    background: radial-gradient(circle, rgba(255,255,255,0.95) 0%, rgba(255,255,255,0.75) 70%);
  }
  .person {
    position: absolute;
    left: 22px;
    top: 134px;
    font-size: 13px;
    color: var(--ink);
  }
  .person-name {
    color: var(--maroon);
    font-weight: 700;
  }
  .contact {
    position: absolute;
    left: 22px;
    top: 202px;
    font-size: 12.5px;
    line-height: 18px;
    color: var(--ink);
    margin: 0;
    font-style: normal;
  }
  .contact-web {
    color: var(--maroon);
  }
  .back-brand {
    position: absolute;
    left: 180px;
    top: 128px;
    display: flex;
    align-items: center;
    gap: 8px;
  }
  .back-brand .brand-mark {
    background: var(--back-text);
  }
  .back-brand .brand-name {
    color: var(--back-text);
    font-size: 20px;
  }
  .back-site {
    position: absolute;
    left: 180px;
    top: 168px;
    font-size: 13px;
    font-weight: 700;
    color: var(--back-text);
  }
</style>
</head>
<body>
<main class="canvas">
  <section class="card card-front" aria-label="Card front">
    <div class="brand">
      <span class="brand-mark"></span>
      <span class="brand-name">Copperleaf Grill</span>
    </div>
    <div class="brand-city">New Orleans</div>
    <div class="artwork artwork-front" role="img" aria-label="Large maroon bird illustration"></div>
    <div class="person"><span class="person-name">Danielle Whitcomb</span> Proprietor</div>
    <address class="contact">
      318 Ferrand Street New Orleans, LA 70119<br>
      Phone: 504.555.0142 / Cell: 504.555.0187<br>
      Email: dwhitcomb@copperleaf-eats.com<br>
      <span class="contact-web">:: www.copperleaf-eats.com ::</span>
    </address>
  </section>
  <section class="card card-back" aria-label="Card back">
    <div class="artwork artwork-back" role="img" aria-label="Large white bird illustration"></div>
    <div class="back-brand">
      <span class="brand-mark"></span>
      <span class="brand-name">Copperleaf Grill</span>
    </div>
    <div class="back-site">:: www.copperleaf-eats.com ::</div>
  </section>
</main>
</body>
</html>
```